Resume: Professional Marketer seeking to impress potential recruiters with my skills & experience

Create a marketing esque style CV. I'm an outgoing, driven marketing with years of experience. I'm looking for a new senior role. My CV should look professional, but with elements of creativity and be a little bold. It should stand out amongst all the other CVs being submitted for a role. Check out my crewbase profile here: https://www.crewbase.example/in/marisol-tovrek-58210394/ I would like to include a photo with the design, as a subtle element of the design.

Target Market(s)

Recruiters, Headhunters

Industry/Entity Type

Marketing

Font styles to use
Sans Serif

Requirements
Must have
• Easy to read sections, with enough detail for a recruiter to understand my experience.
Nice to have
• Graphics, icons etc to represent experience

```html
<!DOCTYPE html>
<html lang="en">
<head>
<meta charset="utf-8">
<title>Marisol Tovrek – Curriculum Vitae</title>
<link rel="stylesheet" href="https://fonts.googleapis.com/css2?family=Oswald:wght@400;500&family=Arimo:wght@400;700&display=swap">
<style>
:root{
  --bg-dark:#3a3a3a;
  --bg-mid:#555555;
  --paper:#ffffff;
  --ink:#4a4a4a;
  --ink-soft:#666666;
  --rule:#555555;
  --row-alt:#f3f3f5;
  --row-line:#dcdce2;
  --photo-a:#b99a82;
  --photo-b:#8a6d5a;
}
*{margin:0;padding:0;box-sizing:border-box}
html,body{width:1200px;height:1200px;overflow:hidden}
body{background:radial-gradient(ellipse at 50% 45%,var(--bg-mid),var(--bg-dark) 75%);position:relative;font-family:"Arimo",Arial,sans-serif;color:var(--ink)}
.page{position:absolute;background:var(--paper);overflow:hidden}
.page--cover{left:400px;top:22px;width:403px;height:570px}
.page--skills{left:174px;top:607px;width:400px;height:570px}
.page--experience{left:626px;top:607px;width:400px;height:570px}
.abs{position:absolute}
.name{position:absolute;left:0;right:0;text-align:center;font-family:"Oswald",sans-serif;font-weight:500;color:var(--ink);letter-spacing:1px;font-variant:small-caps;text-transform:lowercase}
.page--cover .name{top:16px;font-size:38px;line-height:1}
.page--skills .name,.page--experience .name{top:12px;font-size:29px;line-height:1}
.name-bar{position:absolute;height:3px;background:var(--ink)}
.section-head{position:absolute;display:flex;align-items:center;gap:6px;font-family:"Oswald",sans-serif;font-weight:500;color:var(--ink);text-transform:uppercase;line-height:1}
.section-head svg{flex:none}
.rule{position:absolute;height:1px;background:var(--rule)}
.photo{position:absolute;left:33px;top:100px;width:98px;height:98px;background:linear-gradient(160deg,var(--photo-a),var(--photo-b))}
.profile-text{position:absolute;left:34px;top:240px;width:98px;font-size:7px;line-height:9.8px;color:var(--ink-soft)}
.profile-text p{margin-bottom:7px}
.contact-list{position:absolute;left:194px;top:123px;font-size:7px;color:var(--ink-soft)}
.contact-list li{list-style:none;display:flex;align-items:center;gap:3px;height:16px}
.entries{position:absolute;left:169px;font-size:7px;line-height:9.9px;color:var(--ink-soft)}
.entries div{margin-bottom:9.9px}
.skills-grid{position:absolute;left:38px;top:92px;display:grid;grid-template-columns:124px 110px 120px;row-gap:6.6px;font-size:7px;color:var(--ink-soft)}
.skill{display:flex;align-items:center;gap:6px;height:11px}
.skill svg{flex:none}
.employment{position:absolute;left:43px;top:289px;width:323px;border-collapse:collapse;font-size:6.8px;color:var(--ink-soft);line-height:8.6px}
.employment td{border-bottom:1px solid var(--row-line);padding:1.5px 4px;vertical-align:top}
.employment tr:nth-child(odd) td{background:var(--row-alt)}
.employment td:first-child{width:86px;border-right:1px solid var(--row-line)}
.job{position:absolute;left:0;width:374px;font-size:7px;line-height:8.6px;color:var(--ink-soft)}
.job-dates{position:absolute;right:262px;top:0;white-space:nowrap}
.job-body{position:absolute;left:153px;top:0;width:221px}
.job-body strong{display:block;color:var(--ink);font-weight:700;margin-bottom:2px}
</style>
</head>
<body>

<!-- Cover page -->
<section class="page page--cover">
  <h1 class="name">Marisol&nbsp; Tovrek</h1>
  <div class="name-bar" style="left:164px;top:74px;width:77px"></div>

  <div class="photo" role="img" aria-label="Portrait photo of Marisol Tovrek"></div>

  <div class="section-head" style="left:31px;top:210px;font-size:19px">
    <svg width="23" height="23" viewBox="0 0 24 24"><circle cx="12" cy="12" r="12" fill="#4a4a4a"/><circle cx="12" cy="9" r="3.6" fill="#fff"/><path d="M5.5 18c1-3.5 3.6-5 6.5-5s5.5 1.5 6.5 5z" fill="#fff"/></svg>
    Profile <span style="font-weight:400">—</span>
  </div>
  <div class="profile-text">
    <p>I am a passionate direct marketer of 15+ years experience in Australia, plus key roles in startup organisations in London and New York.</p>
    <p>I am a talented consumer marketer with strong commercial and business acumen. I played a fundamental role in the growth of SureLine Direct Pty Ltd, to become the number one direct life insurance brand in Australia.</p>
    <p>As a strategic marketer, my strengths lie in analytical thinking and the ability to translate marketing and sales activity into commercial modeling, and ultimately profitability.</p>
    <p>My goals are to engage with as many strategic and intellectual minds as possible, and to help others develop to achieve theirs.</p>
  </div>

  <div class="section-head" style="left:163px;top:99px;font-size:19px">
    <svg width="23" height="23" viewBox="0 0 24 24"><circle cx="12" cy="12" r="12" fill="#4a4a4a"/><rect x="6" y="7.5" width="12" height="9" rx="1" fill="#fff"/><circle cx="9.5" cy="11" r="1.5" fill="#4a4a4a"/><rect x="12.5" y="10" width="4" height="1" fill="#4a4a4a"/><rect x="12.5" y="12.5" width="4" height="1" fill="#4a4a4a"/></svg>
    Contact
  </div>
  <div class="rule" style="left:258px;top:111px;width:124px"></div>
  <ul class="contact-list">
    <li><svg width="10" height="11" viewBox="0 0 10 12"><path d="M5 11.5S1 7 1 4.5a4 4 0 0 1 8 0C9 7 5 11.5 5 11.5z" fill="none" stroke="#4a4a4a" stroke-width="0.9"/><circle cx="5" cy="4.5" r="1.4" fill="none" stroke="#4a4a4a" stroke-width="0.9"/></svg>Harlow Bay NSW</li>
    <li><svg width="10" height="11" viewBox="0 0 10 12"><rect x="2" y="0.5" width="6.5" height="11" rx="1" fill="none" stroke="#4a4a4a" stroke-width="1"/></svg>0400 555 318</li>
    <li><span style="font-size:12px;color:#4a4a4a;line-height:1">@</span>marisolt@mailpost.example</li>
  </ul>

  <div class="section-head" style="left:165px;top:187px;font-size:19px">
    <svg width="23" height="23" viewBox="0 0 24 24"><circle cx="12" cy="12" r="12" fill="#4a4a4a"/><path d="M4.5 10.5L12 7l7.5 3.5L12 14z" fill="#fff"/><path d="M8 12.5v3c2.5 1.6 5.5 1.6 8 0v-3L12 14.5z" fill="#fff"/></svg>
    Education
  </div>
  <div class="rule" style="left:274px;top:198px;width:109px"></div>
  <div class="entries" style="top:214px">
    <div>Veralta Limited<br>April 2012 – Current<br>Veralta Senior Leaders Strategy Program</div>
    <div>Veralta Limited<br>February 2009 – April 2010<br>Equip Leadership Program</div>
    <div>Kestrel Business Academy, VIC<br>October 2008 – Completed<br>Certificate IV in Business, Frontline Management</div>
    <div>Eastbridge University, Sydney<br>January 1993 – June 1997<br>Bachelor of Business,<br>Major in Marketing and Small Business</div>
  </div>

  <div class="section-head" style="left:164px;top:391px;font-size:19px">
    <svg width="23" height="23" viewBox="0 0 24 24"><circle cx="12" cy="12" r="12" fill="#4a4a4a"/><circle cx="12" cy="10" r="4.2" fill="#fff"/><circle cx="12" cy="10" r="2" fill="#4a4a4a"/><path d="M9.5 13.5L8.5 19l3.5-2 3.5 2-1-5.5z" fill="#fff"/></svg>
    Award
  </div>
  <div class="rule" style="left:252px;top:405px;width:129px"></div>
  <div class="entries" style="top:420px">
    <div>Overall Company Achievement Award 2009<br>Veralta Limited<br>December 2009</div>
    <div>Outstanding Achievement Award 2009<br>Veralta Limited<br>December 2008</div>
    <div>Employee of the Year Award 2005<br>SureLine Direct Pty Ltd<br>December 2005</div>
  </div>
</section>

<!-- Skills & employment page -->
<section class="page page--skills">
  <h2 class="name">Marisol&nbsp; Tovrek</h2>
  <div class="name-bar" style="left:182px;top:47px;width:38px"></div>

  <div class="section-head" style="left:35px;top:55px;font-size:18px">
    <svg width="22" height="22" viewBox="0 0 24 24"><circle cx="12" cy="12" r="12" fill="#4a4a4a"/><circle cx="10" cy="13" r="3.5" fill="none" stroke="#fff" stroke-width="2"/><circle cx="15.5" cy="8.5" r="2" fill="none" stroke="#fff" stroke-width="1.6"/></svg>
    Skills
  </div>
  <div class="rule" style="left:127px;top:69px;width:249px"></div>

  <div class="skills-grid">
    <div class="skill"><svg width="11" height="11"><rect x=".5" y=".5" width="10" height="10" rx="2" fill="none" stroke="#777"/></svg>Advertising</div>
    <div class="skill"><svg width="11" height="11"><rect x=".5" y=".5" width="10" height="10" rx="2" fill="none" stroke="#777"/></svg>Digital Marketing</div>
    <div class="skill"><svg width="11" height="11"><circle cx="5.5" cy="5.5" r="5" fill="none" stroke="#777"/></svg>Media Planning</div>
    <div class="skill"><svg width="11" height="11"><rect x=".5" y=".5" width="10" height="10" rx="2" fill="none" stroke="#777"/></svg>Branding</div>
    <div class="skill"><svg width="11" height="11"><rect x=".5" y=".5" width="10" height="10" rx="2" fill="none" stroke="#777"/></svg>Distribution</div>
    <div class="skill"><svg width="11" height="11"><circle cx="5.5" cy="5.5" r="5" fill="none" stroke="#777"/></svg>People Management</div>
    <div class="skill"><svg width="11" height="11"><rect x=".5" y=".5" width="10" height="10" rx="2" fill="none" stroke="#777"/></svg>Budgeting &amp; Forecasting</div>
    <div class="skill"><svg width="11" height="11"><rect x=".5" y=".5" width="10" height="10" rx="2" fill="none" stroke="#777"/></svg>Direct Marketing</div>
    <div class="skill"><svg width="11" height="11"><circle cx="5.5" cy="5.5" r="5" fill="none" stroke="#777"/></svg>Product Development</div>
    <div class="skill"><svg width="11" height="11"><rect x=".5" y=".5" width="10" height="10" rx="2" fill="none" stroke="#777"/></svg>Business Analysis</div>
    <div class="skill"><svg width="11" height="11"><rect x=".5" y=".5" width="10" height="10" rx="2" fill="none" stroke="#777"/></svg>Executive Reporting</div>
    <div class="skill"><svg width="11" height="11"><circle cx="5.5" cy="5.5" r="5" fill="none" stroke="#777"/></svg>P&amp;L Responsibility</div>
    <div class="skill"><svg width="11" height="11"><rect x=".5" y=".5" width="10" height="10" rx="2" fill="none" stroke="#777"/></svg>Call Centres</div>
    <div class="skill"><svg width="11" height="11"><rect x=".5" y=".5" width="10" height="10" rx="2" fill="none" stroke="#777"/></svg>Financial Modelling</div>
    <div class="skill"><svg width="11" height="11"><circle cx="5.5" cy="5.5" r="5" fill="none" stroke="#777"/></svg>Retention</div>
    <div class="skill"><svg width="11" height="11"><rect x=".5" y=".5" width="10" height="10" rx="2" fill="none" stroke="#777"/></svg>Customer Acquisition</div>
    <div class="skill"><svg width="11" height="11"><rect x=".5" y=".5" width="10" height="10" rx="2" fill="none" stroke="#777"/></svg>Lead Generation</div>
    <div class="skill"><svg width="11" height="11"><circle cx="5.5" cy="5.5" r="5" fill="none" stroke="#777"/></svg>Sales</div>
    <div class="skill"><svg width="11" height="11"><rect x=".5" y=".5" width="10" height="10" rx="2" fill="none" stroke="#777"/></svg>Customer Retention</div>
    <div class="skill"><svg width="11" height="11"><rect x=".5" y=".5" width="10" height="10" rx="2" fill="none" stroke="#777"/></svg>Marketing Analysis</div>
    <div class="skill"><svg width="11" height="11"><circle cx="5.5" cy="5.5" r="5" fill="none" stroke="#777"/></svg>Strategy Development</div>
    <div class="skill"><svg width="11" height="11"><rect x=".5" y=".5" width="10" height="10" rx="2" fill="none" stroke="#777"/></svg>Copy Writing</div>
    <div class="skill"><svg width="11" height="11"><rect x=".5" y=".5" width="10" height="10" rx="2" fill="none" stroke="#777"/></svg>Marketing</div>
    <div class="skill"><svg width="11" height="11"><circle cx="5.5" cy="5.5" r="5" fill="none" stroke="#777"/></svg>Stakeholder Management</div>
  </div>

  <div class="section-head" style="left:39px;top:254px;font-size:18px">
    <svg width="22" height="22" viewBox="0 0 24 24"><circle cx="12" cy="12" r="12" fill="#4a4a4a"/><rect x="7" y="7.5" width="2" height="2" fill="#fff"/><rect x="10.5" y="7.5" width="7" height="2" fill="#fff"/><rect x="7" y="11" width="2" height="2" fill="#fff"/><rect x="10.5" y="11" width="7" height="2" fill="#fff"/><rect x="7" y="14.5" width="2" height="2" fill="#fff"/><rect x="10.5" y="14.5" width="7" height="2" fill="#fff"/></svg>
    Employment Record
  </div>
  <div class="rule" style="left:231px;top:265px;width:143px"></div>

  <table class="employment">
    <tr><td>May 2016 – Current</td><td>Marketing Strategy Consultant<br>at SpokeNotes, Alpine Re, Harbour Lane Studio</td></tr>
    <tr><td>Jan 2011 – Current</td><td>Marketer and Business Development at Ralph Okoye Photography</td></tr>
    <tr><td>Aug 2015 – May 2016</td><td>Career break</td></tr>
    <tr><td>Apr 2015 – Aug 2015</td><td>Head of Marketing at Meridian Life Distribution (US)</td></tr>
    <tr><td>Aug 2014 – Apr 2015</td><td>Maternity Leave – to my son Theo</td></tr>
    <tr><td>Mar 2014 – Aug 2014</td><td>General Manager Marketing and Business Operations<br>at Meridian Life Distribution (US)</td></tr>
    <tr><td>May 2013 – Apr 2014</td><td>Career Break</td></tr>
    <tr><td>Oct 2013</td><td>Consultant – New Business Proposal at Brightwater Administration Services Pty Ltd</td></tr>
    <tr><td>Dec 2012 – May 2013</td><td>Commercial &amp; MIS Manager at Veralta Limited</td></tr>
    <tr><td>Jul 2012 – Dec 2012</td><td>Head of Marketing Operations at Veralta Limited</td></tr>
    <tr><td>Oct 2010 – Dec 2012</td><td>P&amp;L / Brand Manager at Veralta Limited</td></tr>
    <tr><td>Jan 2010 – Oct 2010</td><td>Product Portfolio Marketing at Veralta Limited</td></tr>
    <tr><td>Jan 2008 – Oct 2010</td><td>Marketing Manager at Veralta Limited</td></tr>
    <tr><td>Feb 2007 – Dec 2007</td><td>Database and Retention Strategy Manager at SureLine Direct Pty Ltd</td></tr>
    <tr><td>Jul 2004 – Jan 2007</td><td>Direct Marketing Specialist at SureLine Direct Pty Ltd</td></tr>
    <tr><td>Apr 2002 – Jun 2004</td><td>Acquisition and Database Marketing Manager - Japan<br>at Rewardworks Pty Ltd</td></tr>
  </table>
</section>

<!-- Experience page -->
<section class="page page--experience">
  <h2 class="name">Marisol&nbsp; Tovrek</h2>
  <div class="name-bar" style="left:181px;top:45px;width:38px"></div>

  <div class="section-head" style="left:43px;top:63px;font-size:18px">
    <svg width="22" height="22" viewBox="0 0 24 24"><circle cx="12" cy="12" r="12" fill="#4a4a4a"/><rect x="6" y="8.5" width="12" height="8.5" rx="1" fill="#fff"/><rect x="9.5" y="6.5" width="5" height="2.5" fill="none" stroke="#fff" stroke-width="1.2"/></svg>
    Experience
  </div>
  <div class="rule" style="left:163px;top:74px;width:210px"></div>

  <div class="job" style="top:110px"><span class="job-dates">May 2016 &nbsp;- &nbsp;May 2018</span><div class="job-body"><strong>Marketing Strategy Consultant</strong>Clients include SpokeNotes, Alpine Re, Harbour Lane Studio, Table Ready, Coastal Health Fund.</div></div>
  <div class="job" style="top:155px"><span class="job-dates">Apr 2015 &nbsp;- &nbsp;Aug 2015</span><div class="job-body"><strong>Head of Marketing</strong>Meridian Life Distribution (US) - Keepsake Life, consumer life insurance brand<br>Key stakeholder relationships with;<br>Five owners of Meridian Life Distribution, Alpine Re US (a reinsurer), and NBLA (the insurance company).</div></div>
  <div class="job" style="top:230px"><span class="job-dates">Mar 2014 &nbsp;- &nbsp;Aug 2014</span><div class="job-body"><strong>Head of Marketing &amp; General Manager - Business Operations</strong>Meridian Life Distribution (UK) - Pledge Life, consumer life insurance brand<br>Key stakeholder relationships with;<br>Five owners of Meridian Life Distributions, including Alpine Re UK</div></div>
  <div class="job" style="top:296px"><span class="job-dates">Dec 2012 &nbsp;- &nbsp;May 2013</span><div class="job-body"><strong>Commercial &amp; MIS Advisor</strong>Veralta Limited<br>Primary Customer Engagement will be with;<br>The Commercial Director ; The Chief Customer Officer<br>Chief Marketing Officer</div></div>
  <div class="job" style="top:358px"><span class="job-dates">Dec 2012 &nbsp;- &nbsp;May 2013</span><div class="job-body"><strong>Head of Marketing Operations – Acquisition and Retention</strong>Veralta Limited<br>The Head of Marketing Operations engages with senior leadership; delivering outcomes by influencing and leading others.</div></div>
  <div class="job" style="top:406px"><span class="job-dates">Jul 2012 &nbsp;- &nbsp;Dec 2012</span><div class="job-body"><strong>Head of Marketing Operations – Acquisition and Retention</strong>Veralta Limited</div></div>
  <div class="job" style="top:438px"><span class="job-dates">Oct 2010 &nbsp;- &nbsp;Jul 2012</span><div class="job-body"><strong>P&amp;L / Brand Manager – SureLine Direct</strong>Part of the BEACON Group</div></div>
  <div class="job" style="top:470px"><span class="job-dates">Jan 2010 &nbsp;- &nbsp;Oct 2010</span><div class="job-body"><strong>Product Portfolio Marketing Manager – SureLine Direct</strong>Part of the BEACON Group</div></div>
  <div class="job" style="top:502px"><span class="job-dates">Jan 2008 &nbsp;- &nbsp;Oct 2010</span><div class="job-body"><strong>Marketing Manager</strong>SureLine Direct Pty Ltd</div></div>
</section>

</body>
</html>
```